Copper Finch Agency Website - Wordpress Web UPDATED BRIEF

FINAL LOGO UPLOADED - please look to this as reference for how we would like the site to look and feel.

We are a digital marketing agency - looking to have a new website built. We are looking for a simple one page feel of site that will allow us to grow it later. (Feel free to take some liberties with that if your imagination veers off) Must be very, playful, bold, sleek and easily integrate video. Wordpress only.

Overview:

Copper Finch is a creative constellation. We are built on what's great about the shared economy. With access to thousands of content creators, designers, technicians, writers, strategists and other creatives around the world, we are built differently than a traditional “brick and mortar” Marketing Agency. We provide the traditional services our clients have come to expect, without the “5X factor” of covering the overhead common in the old agency model. We believe even better work can be created in collaboration with our clients and by passing those savings back to them for their use. Our clients pay for our art, our work and our passion –not our furniture.

"Copper Finch, Let's Start Something"

Target Market(s)

companies looking for creative agency help, video production, creative consulting and coaching

Industry/Entity Type

Digital Marketing

Coding

Coded - Design and coding required

Number of Pages Required

1 page

Font styles to use
Sans Serif

Colors
3277b5
33a6d7
ec1f27

Requirements
Must have
• Wordpress design is a must. Looking for a one sheet homepage - with sections that are all on the main front page. We will have videos to embed, and should be able to have client logos and easy access to show a variety of our creative work.
• Please look to the logo for how we would like the site to feel.
• Please think "icon process flow" instead of blocks of text (which we used to have). Use the text to explain what the process flow should represent - don't actually copy paste the text but show it visually in icons.
Nice to have
• innovation around how we show video content. solid colors complementary to our palette and aesthetic.
Should not have
• Standard HTML coding

```html
<!DOCTYPE html>
<html lang="en">
<head>
<meta charset="utf-8">
<title>Copper Finch Agency</title>
<link rel="stylesheet" href="https://fonts.googleapis.com/css2?family=Merriweather:wght@400;700&family=Roboto:wght@400;500;700&display=swap">
<style>
:root{
  --blue:#3277b5;
  --sky:#33a6d7;
  --red:#ec1f27;
  --ink:#222831;
  --muted:#6b7380;
  --line:#d9dde3;
  --white:#ffffff;
  --mist:#f1f3f6;
  --serif:'Merriweather', Georgia, serif;
  --sans:'Roboto', Arial, sans-serif;
}
*{box-sizing:border-box;margin:0;padding:0}
html,body{width:1200px;height:4372px;overflow:hidden}
body{font-family:var(--sans);color:var(--ink);background:var(--white);position:relative}
section,header,footer{position:relative;width:1200px;overflow:hidden}

/* header */
.site-header{height:180px;background:var(--white)}
.topbar{position:absolute;right:48px;top:22px;display:flex;gap:28px;font-size:14px;color:var(--ink)}
.topbar span{display:flex;align-items:center;gap:8px}
.brand{position:absolute;left:70px;top:40px;display:flex;align-items:center;gap:12px}
.brand-dot{width:70px;height:70px;border-radius:50%;background:var(--blue)}
.brand-name{font-family:var(--sans);font-weight:700;font-size:24px;color:var(--blue)}
.nav{position:absolute;right:48px;top:92px;display:flex;gap:30px;font-size:16px;font-weight:500}

/* hero */
.hero{height:620px;background:linear-gradient(120deg,#1d2a44 0%,#2d3f63 45%,#3a4a7a 70%,#4b3c73 100%)}
.hero-media{position:absolute;inset:0}
.hero-copy{position:absolute;left:88px;top:190px;width:500px;color:var(--white)}
.hero-title{font-family:var(--serif);font-size:50px;font-weight:700;margin-bottom:14px}
.hero-text{font-size:17px;line-height:1.5;margin-bottom:26px}
.btn-outline{display:inline-block;border:2px solid var(--white);border-radius:24px;padding:12px 24px;font-size:15px;font-weight:700;color:var(--white)}
.slide-arrow{position:absolute;top:290px;width:36px;height:36px;border-radius:50%;background:rgba(255,255,255,.85);display:flex;align-items:center;justify-content:center}
.slide-arrow.left{left:20px}.slide-arrow.right{right:20px}

/* about */
.about{height:680px;background:var(--red)}
.about-frame{position:absolute;left:280px;top:60px;width:816px;height:510px;border:2px solid rgba(255,255,255,.85)}
.about-media{position:absolute;left:120px;top:100px;width:250px;height:290px;background:linear-gradient(135deg,#1f3f78,#3277b5 60%,#7aa7d6)}
.about-copy{position:absolute;left:520px;top:100px;width:440px;color:var(--white)}
.about-title{font-family:var(--serif);font-size:38px;font-weight:700;margin-bottom:18px}
.about-text{font-size:16px;line-height:1.55;margin-bottom:28px}
.btn-blue{display:inline-block;background:var(--blue);border-radius:24px;padding:13px 26px;font-size:14px;font-weight:700;color:var(--white)}

/* services */
.services{height:540px;background:linear-gradient(180deg,#f6f7f9,#eef0f3)}
.section-title{font-family:var(--serif);font-size:40px;font-weight:700;text-align:center;color:var(--ink)}
.services .section-title{padding-top:40px}
.flow{position:absolute;left:0;top:150px}

/* gallery */
.gallery{height:1100px;background:var(--white)}
.gallery .section-title{padding-top:96px}
.tile{position:absolute}
.t1{left:192px;top:220px;width:268px;height:280px;background:linear-gradient(135deg,#4a3a30,#8a6a50)}
.t2{left:468px;top:220px;width:272px;height:280px;background:linear-gradient(135deg,#2e2a30,#a07048)}
.t3{left:748px;top:220px;width:260px;height:280px;background:linear-gradient(135deg,#cfd6de,#7c8796)}
.t4{left:192px;top:510px;width:268px;height:290px;background:linear-gradient(135deg,#c4c9cf,#d9473a 60%,#33a6d7)}
.t5{left:468px;top:510px;width:540px;height:290px;background:linear-gradient(135deg,#2b2b30,#c97a3a 55%,#e2e2e2)}
.t6{left:192px;top:810px;width:548px;height:290px;background:linear-gradient(135deg,#3a3f47,#78818c)}
.t7{left:748px;top:810px;width:260px;height:290px;background:linear-gradient(135deg,#1f2a38,#4a5a70)}
.t6-label{position:absolute;left:110px;top:118px;font-family:var(--sans);font-weight:700;font-size:38px;color:var(--white)}

/* testimonial */
.testimonial{height:600px;background:linear-gradient(180deg,#f3f4f6,#e8eaee)}
.quote-marks{position:absolute;left:0;right:0;top:80px;text-align:center;font-family:var(--serif);font-size:60px;color:#c8ccd2;letter-spacing:140px;padding-left:140px}
.stars{position:absolute;left:0;right:0;top:104px;text-align:center;color:#f2a51a;font-size:18px;letter-spacing:3px}
.quote-text{position:absolute;left:300px;width:600px;top:150px;text-align:center;font-size:15px;line-height:1.6;color:var(--ink)}
.avatars{position:absolute;left:0;right:0;top:230px;display:flex;justify-content:center;align-items:center;gap:24px}
.avatar{border-radius:50%;background:linear-gradient(135deg,#b9bec6,#8d939c)}
.avatar.sm{width:52px;height:52px}.avatar.lg{width:82px;height:82px;background:linear-gradient(135deg,#9aa1ab,#5d6470)}
.person{position:absolute;left:0;right:0;top:330px;text-align:center;font-size:15px}
.person small{display:block;color:var(--muted);font-size:13px;margin-top:4px}
.t-arrow{position:absolute;top:240px;width:32px;height:32px;border-radius:50%;display:flex;align-items:center;justify-content:center}
.t-arrow.left{left:24px;background:var(--blue)}.t-arrow.right{right:24px;background:var(--red)}

/* partners */
.partners{height:320px;background:var(--white)}
.partners .section-title{padding-top:28px}
.partner-card{position:absolute;left:190px;top:110px;width:830px;height:120px;background:var(--white);box-shadow:0 4px 18px rgba(0,0,0,.12);display:flex;justify-content:space-around;align-items:center}
.partner-badge{width:190px;height:64px;border-radius:8px;background:var(--mist)}
.pager{position:absolute;right:196px;top:78px;display:flex;gap:8px}
.pager span{width:22px;height:22px;border-radius:50%}

/* footer */
.site-footer{height:332px;background:var(--blue);color:var(--white)}
.footer-cols{position:absolute;left:92px;top:40px;display:flex;gap:0}
.fcol h4{font-size:18px;font-weight:500;margin-bottom:14px}
.fcol p,.fcol li{font-size:14px;line-height:1.45;list-style:none}
.fcol.contact{width:342px}.fcol.links{width:200px}.fcol.touch{width:226px}.fcol.news{width:250px}
.fcol .label{margin-top:10px}
.touch li{display:flex;align-items:center;gap:10px;margin-bottom:8px}
.touch li i{width:18px;height:18px;border-radius:50%;background:var(--white);display:inline-block}
.news-form{display:flex;margin-top:14px}
.news-form span{flex:1;background:var(--white);color:#9aa0a8;font-size:12px;padding:9px 10px}
.news-form b{width:36px;background:#1f5a93;display:flex;align-items:center;justify-content:center}
.copyright{position:absolute;left:0;right:0;bottom:18px;text-align:center;font-size:12px;opacity:.85}
</style>
</head>
<body>

<header class="site-header">
  <div class="topbar">
    <span><svg width="14" height="14" viewBox="0 0 24 24"><path d="M6.6 10.8a15 15 0 0 0 6.6 6.6l2.2-2.2c.3-.3.7-.4 1-.2 1.1.4 2.3.6 3.6.6.6 0 1 .4 1 1V20c0 .6-.4 1-1 1A17 17 0 0 1 3 4c0-.6.4-1 1-1h3.5c.6 0 1 .4 1 1 0 1.3.2 2.5.6 3.6.1.3 0 .7-.2 1z" fill="#3277b5"/></svg>555-014-2290</span>
    <span><svg width="16" height="12" viewBox="0 0 16 12"><rect x="0.5" y="0.5" width="15" height="11" fill="none" stroke="#3277b5"/><path d="M1 1l7 6 7-6" fill="none" stroke="#3277b5"/></svg>info@copperfinch.com</span>
  </div>
  <div class="brand"><span class="brand-dot"></span><span class="brand-name">Copper Finch</span></div>
  <nav class="nav"><span>Home</span><span>About Us</span><span>Services</span><span>Our Clients</span><span>Testimonials</span><span>Gallery</span><span>Contact Us</span></nav>
</header>

<section class="hero">
  <div class="hero-media" role="img" aria-label="Hands using a smartphone surrounded by glowing digital network lines"></div>
  <div class="slide-arrow left"><svg width="12" height="12" viewBox="0 0 12 12"><path d="M8 1L3 6l5 5" stroke="#222831" stroke-width="2" fill="none"/></svg></div>
  <div class="slide-arrow right"><svg width="12" height="12" viewBox="0 0 12 12"><path d="M4 1l5 5-5 5" stroke="#222831" stroke-width="2" fill="none"/></svg></div>
  <div class="hero-copy">
    <h1 class="hero-title">Copper Finch</h1>
    <p class="hero-text">We are built on what's great about the shared economy with access to thousands of content creators, designers, technicians.</p>
    <span class="btn-outline">REQUEST A QUOTE</span>
  </div>
</section>

<section class="about">
  <div class="about-frame"></div>
  <div class="about-media" role="img" aria-label="Digital marketing concept photo with a hand touching a screen"></div>
  <div class="about-copy">
    <h2 class="about-title">ABOUT US</h2>
    <p class="about-text">Copper Finch is a creative constellation. We are built on what's great about the shared economy. With access to thousands of content creators, designers, technicians, writers, strategists and other creatives around the world, we are built differently than a traditional “brick and mortar” Marketing Agency. We provide the traditional services our clients have come to expect, without</p>
    <span class="btn-blue">READ MORE</span>
  </div>
</section>

<section class="services">
  <h2 class="section-title">OUR SERVICES</h2>
  <svg class="flow" width="1200" height="360" viewBox="0 0 1200 360" font-family="Roboto, Arial, sans-serif">
    <line x1="150" y1="160" x2="1050" y2="160" stroke="#d9dde3" stroke-width="4"/>
    <g fill="none" stroke-width="14">
      <!-- 01 -->
      <circle cx="150" cy="160" r="62" stroke="#d9dde3"/><path d="M88 160a62 62 0 0 1 124 0" stroke="#3277b5"/>
      <!-- 02 -->
      <circle cx="300" cy="160" r="62" stroke="#d9dde3"/><path d="M238 160a62 62 0 0 0 124 0" stroke="#ec1f27"/>
      <!-- 03 -->
      <circle cx="450" cy="160" r="62" stroke="#d9dde3"/><path d="M388 160a62 62 0 0 1 124 0" stroke="#3277b5"/>
      <!-- 04 -->
      <circle cx="600" cy="160" r="62" stroke="#d9dde3"/><path d="M538 160a62 62 0 0 0 124 0" stroke="#ec1f27"/>
      <!-- 05 -->
      <circle cx="750" cy="160" r="62" stroke="#d9dde3"/><path d="M688 160a62 62 0 0 1 124 0" stroke="#3277b5"/>
      <!-- 06 -->
      <circle cx="900" cy="160" r="62" stroke="#d9dde3"/><path d="M838 160a62 62 0 0 0 124 0" stroke="#ec1f27"/>
      <!-- 07 -->
      <circle cx="1050" cy="160" r="62" stroke="#d9dde3"/><path d="M988 160a62 62 0 0 1 124 0" stroke="#3277b5"/>
    </g>
    <g fill="#ffffff">
      <circle cx="150" cy="160" r="54"/><circle cx="300" cy="160" r="54"/><circle cx="450" cy="160" r="54"/><circle cx="600" cy="160" r="54"/><circle cx="750" cy="160" r="54"/><circle cx="900" cy="160" r="54"/><circle cx="1050" cy="160" r="54"/>
    </g>
    <g fill="none" stroke="#222831" stroke-width="2.5">
      <circle cx="146" cy="156" r="13"/><path d="M155 165l11 11"/>
      <circle cx="300" cy="160" r="16"/><circle cx="300" cy="160" r="8"/><circle cx="300" cy="160" r="2" fill="#222831"/>
      <rect x="434" y="146" width="32" height="26" rx="2"/><path d="M434 154h32M442 142v8M458 142v8"/>
      <rect x="586" y="144" width="28" height="32" rx="2"/><path d="M592 154h16M592 161h16M592 168h10"/>
      <rect x="734" y="148" width="24" height="22" rx="2"/><path d="M758 154l10-6v22l-10-6"/>
      <path d="M884 174v-12M895 174v-20M906 174v-28M917 174v-16"/>
      <circle cx="1050" cy="150" r="9"/><path d="M1034 178c2-12 30-12 32 0"/>
    </g>
    <g font-size="15" text-anchor="middle" fill="#222831">
      <text x="150" y="265" font-size="22" font-weight="700" fill="#3277b5">01</text><text x="150" y="288">Discovery</text>
      <text x="300" y="56" font-size="22" font-weight="700" fill="#3277b5">02</text><text x="300" y="78">Strategy</text>
      <text x="450" y="265" font-size="22" font-weight="700" fill="#3277b5">03</text><text x="450" y="288">Project</text><text x="450" y="307">Management</text>
      <text x="600" y="56" font-size="22" font-weight="700" fill="#3277b5">04</text><text x="600" y="78">Content</text>
      <text x="750" y="265" font-size="22" font-weight="700" fill="#3277b5">05</text><text x="750" y="288">Production</text>
      <text x="900" y="56" font-size="22" font-weight="700" fill="#3277b5">06</text><text x="900" y="78">Paid Media</text>
      <text x="1050" y="265" font-size="22" font-weight="700" fill="#3277b5">07</text><text x="1050" y="288">Coaching</text>
    </g>
  </svg>
</section>

<section class="gallery">
  <h2 class="section-title">GALLERY</h2>
  <div class="tile t1" role="img" aria-label="Team working together at laptops"></div>
  <div class="tile t2" role="img" aria-label="Colleagues in a meeting around a table"></div>
  <div class="tile t3" role="img" aria-label="Tablet showing analytics dashboard"></div>
  <div class="tile t4" role="img" aria-label="Laptop with colorful charts on screen"></div>
  <div class="tile t5" role="img" aria-label="Hands pointing at printed business charts"></div>
  <div class="tile t6" role="img" aria-label="Outsourcing concept with network icons"><span class="t6-label">OUTSOURCING</span></div>
  <div class="tile t7" role="img" aria-label="Presenter beside a whiteboard"></div>
</section>

<section class="testimonial">
  <div class="quote-marks">“”</div>
  <div class="stars">★★★★★</div>
  <p class="quote-text">"Copper Finch is proving to be a force in the creative consulting industry and we look forward to collaborating with them again in the future."</p>
  <div class="avatars">
    <span class="avatar sm" role="img" aria-label="Client portrait"></span>
    <span class="avatar lg" role="img" aria-label="Client portrait"></span>
    <span class="avatar sm" role="img" aria-label="Client portrait"></span>
  </div>
  <p class="person">Morgan<small>March 17, 2019</small></p>
  <div class="t-arrow left"><svg width="10" height="10" viewBox="0 0 10 10"><path d="M7 1L3 5l4 4" stroke="#fff" stroke-width="2" fill="none"/></svg></div>
  <div class="t-arrow right"><svg width="10" height="10" viewBox="0 0 10 10"><path d="M3 1l4 4-4 4" stroke="#fff" stroke-width="2" fill="none"/></svg></div>
</section>

<section class="partners">
  <h2 class="section-title">OUR PARTNERS</h2>
  <div class="pager"><span style="background:var(--blue)"></span><span style="background:var(--red)"></span></div>
  <div class="partner-card">
    <span class="partner-badge"></span><span class="partner-badge"></span><span class="partner-badge"></span>
  </div>
</section>

<footer class="site-footer">
  <div class="footer-cols">
    <div class="fcol contact">
      <h4>CONTACT US</h4>
      <p>Address :</p><p>412 Alder Row,</p><p>Northbank, VIC</p>
      <p class="label">Call Us :</p><p>555-014-2290</p>
      <p class="label">E - Mail :</p><p>info@copperfinch.com</p>
    </div>
    <div class="fcol links">
      <h4>Quick Links</h4>
      <ul><li>Home</li><li>About Us</li><li>Services</li><li>Our Clients</li><li>Testimonials</li><li>Gallery</li><li>Contact Us</li></ul>
    </div>
    <div class="fcol touch">
      <h4>GET IN TOUCH</h4>
      <ul><li><i></i>Pageline</li><li><i></i>Chirpnet</li><li><i></i>Workweb</li><li><i></i>Snapframe</li></ul>
    </div>
    <div class="fcol news">
      <h4>Newsletter</h4>
      <p>Lorem Ipsum has been the industry's standard dummy text ever since the 1500s.</p>
      <div class="news-form"><span>Enter your email address</span><b><svg width="10" height="10" viewBox="0 0 10 10"><path d="M3 1l4 4-4 4" stroke="#fff" stroke-width="2" fill="none"/></svg></b></div>
    </div>
  </div>
  <p class="copyright">© 2018 Copyright. All Rights Reserved</p>
</footer>

</body>
</html>
```